Internet Privacy Author Seeks Graphic Designer for eBook Title Page Graphic

I need for a Talented, Creative Graphic Design Artist to:
.
1) Design / Create a Title Page for my eBook about Internet Privacy
2) Create 3 other simple Chapter Pages for my eBook
Chapter 1 xxxxx
Chapter 2 xxxxx
Chapter 3 xxxxx
3) Copy and Paste my EXACT content into a right click protected pdf eBook (customer can't Copy or Print the eBook.). I must be able to edit to add future content.
4) www.QuietHarborNet.com
Industry/Entity Type
Internet
Requirements
Must have
- Unique, Creative Graphic Design Skills.
- Should have experience creating eBooks, or eBook Title Pages, please show examples of your work.
- Must follow instructions.
- Abide by a Deadline.
- Good and Friendly communication skills.

```html
<!DOCTYPE html>
<html lang="la">
<head>
<meta charset="utf-8">
<title>Chapter 1 — How to make my surfing safer</title>
<link rel="stylesheet" href="https://fonts.googleapis.com/css2?family=Crimson+Text:wght@400;700&family=Noto+Sans:wght@700&display=swap">
<style>
  :root {
    --page-bg: #ffffff;
    --ink: #111111;
    --heading-ink: #000000;
  }
  html, body {
    margin: 0;
    padding: 0;
    width: 1200px;
    height: 1000px;
    overflow: hidden;
    background: var(--page-bg);
  }
  .page {
    position: relative;
    width: 1200px;
    height: 1000px;
    background: var(--page-bg);
    color: var(--ink);
    font-family: "Crimson Text", Georgia, serif;
  }
  .chapter-label {
    position: absolute;
    left: 380px;
    top: 115px;
    margin: 0;
    font-size: 17px;
    line-height: 20px;
    font-weight: 400;
  }
  .chapter-title {
    position: absolute;
    left: 379px;
    top: 143px;
    margin: 0;
    font-family: Verdana, "Noto Sans", sans-serif;
    font-weight: 700;
    font-size: 21.5px;
    line-height: 26px;
    color: var(--heading-ink);
    letter-spacing: 0.1px;
  }
  .chapter-body {
    position: absolute;
    left: 380px;
    top: 194.25px;
    width: 436px;
    font-size: 15px;
    line-height: 19.5px;
  }
  .chapter-body p {
    margin: 0 0 8px 0;
  }
  .line {
    display: block;
    white-space: nowrap;
    text-align: justify;
    text-align-last: justify;
  }
  .line.last {
    text-align-last: left;
  }
  .page-number {
    position: absolute;
    right: 384px;
    top: 899px;
    margin: 0;
    font-size: 14px;
    line-height: 18px;
  }
</style>
</head>
<body>
<main class="page">
  <p class="chapter-label">Chapter 1</p>
  <h1 class="chapter-title">How to make my surfing safer</h1>

  <section class="chapter-body">
    <p>
      <span class="line">ChaCat. Sed et rem. Igentemporia quibus sequi reperior sunt quis is</span>
      <span class="line">quodipsam rerchiciis dolutas alibus ea dolupidel is magnatem velia</span>
      <span class="line">quam rehento tatur, explaborem fugit hilia nobitio reperionse inima</span>
      <span class="line">acipsam, sum re venet quo illuptatet volorum haritat iantiatium aut</span>
      <span class="line">ex et archit et omnis eat que odicaectis minvel esequamus, aute pel-</span>
      <span class="line">lani quis veni odit rerum volest ipienda natiatiur sunt fugiati anturis</span>
      <span class="line">samus, voluptatia ditiorem net que earcia quatem quo ommoluptae</span>
      <span class="line last">la dolut laboribus aut adi disit postisime praectatur?</span>
    </p>
    <p>
      <span class="line">Ilignam, nis rem re nihic temquid molo quo totaspe llorrum ad unt</span>
      <span class="line">quibus dellabo remquo magnia volut eat esci id quae nosam quo ve-</span>
      <span class="line">lesec umendiam volupta qui utae netur magnihilit alis qui quo ex-</span>
      <span class="line">pliqui con resequi aut vel ma pos audi ommolor millabor rehenima</span>
      <span class="line">con pratempe quae vent eribuscit, as experrum fugia aut ero tem</span>
      <span class="line">faccum dolorunt, est, officid quam restet, ut et ut liquiam uscium,</span>
      <span class="line">assimiliqui doloruntio. Hitatur epudandelit res nonsed milles dolup-</span>
      <span class="line last">tiat eaquat.</span>
    </p>
    <p>
      <span class="line">Iscitat ibeari venecullaut voloresto blatem ut officientem iundis que</span>
      <span class="line">offic to temquam, as acepedis modictur min pa que dollatur, sin cor</span>
      <span class="line last">sust, aliqui ommolorro bea veni blatur?</span>
    </p>
    <p>
      <span class="line">Ihillaut elentis rehendit antio vere solupta poria dollabori abo. Par-</span>
      <span class="line">um et fugia dolorporiore praturitaes inis eosapis sunt atem quunte et</span>
      <span class="line">harchilibus, cum con pore preiur saperun tiorecusant dunti nectur</span>
      <span class="line">arcilique et, ipicipienis aut veliqui acerspi ciumque eicilib uscipici-</span>
      <span class="line">am, opta nonse provitat repre od et hicae num quatestrume nus, aces</span>
      <span class="line">esto ducidest, num doluptatquo occatusanda vel eaquaernam et et</span>
      <span class="line last">inctota et fugit, qui dolluptatus minctur?</span>
    </p>
    <p>
      <span class="line">Ugit occuptas alignim odicide ligent volore deligent pra si idis</span>
      <span class="line">molum nest andem nonse culluptiatus restrum fugiam que plab is</span>
      <span class="line">etur magnatur? Sed quibus, nobit aut fuga. Oribusant vendent ioriae</span>
      <span class="line">pedi dici doloresto magnit aut et quamus utEd magnimolore pratem.</span>
      <span class="line">Nempediore velloris atin eos il moditat erumquodi optatinvene nite</span>
      <span class="line">volecearcium harum digentotaque conse quossint pore volum di re-</span>
      <span class="line">risti orpore porpore mpossitas inime seque doluptate pra quatur ad</span>
    </p>
  </section>

  <p class="page-number">1</p>
</main>
</body>
</html>
```